International MultiIndustry Team Coaching Site

Hello Designers,
We need a redesign of the pages attached.
The design must be engaging and modern, with a focus on the user experience, particularly for the "observations" page. Because this is the main page of the website. It is to be used on a 10'' tablet or desktop, to record observations on the fly, so it must be intuitive and efficient.
The positioning of the metrics and observations and etc, are just a reference. you can switch it up if you feel there is a better way (PLEASE DO ;) ).

There are many categories (color coded with borders in the example hpt_6_observations.jpg) and observation metrics within each category. This is the Key page, because it is the One with the most interactions.

The user should know when it has selected a category (there should be some visual hint) and the different metric widgets should be accounted for.
There are 3: The time widget at the end, numerical widgets (recording more or less numbers), and boolean ones (selected or not).

For the numerical widgets, we show plus and minus characters, but you can change this, being creative, keeping in mind that it must work well on a mobile device and desktop, and must be intuitive and quick.

Set your creativity free with the login screen , home screen, categories secret, events screen, journaling and observations screen .

We would like the site/mobile version to have a very modern look. Something that would be found in very popular and user friendly apps.

***** The events, journaling, category and home screens are getting 2 much attention , please focus also on the observations screen *******
Imagine you are a psychologist tasked with observing the behaviour of teenagers during group work. And you have a tablet on which to record what you observe. Now imagine you need to observe during 3 classes: Biology, Math, Physics (these are events). For each class (event) you will have to record observations in 3 categories: Social Interaction, Leadership, Communication (these are categories).
Example of the metrics (these are observations) for Leadership:
" the teenager direct other colleagues" (boolean widget),
"the teenager speaks more than everyone else" (boolean widget)
"the teenager interrupts colleagues speaking" (number widget)
"the work took hh:mm" (time widget)

The observations screen can have any shape and form you think of. It doesn't need to be that single column with yes and nos, or that double column with the squared cards.
thank you.

Hope that was useful intel :)
Available for any questions you might have.
Good luck :)

Enterprise teams

5+ page

Sans Serif

• Modern design

```html
<!DOCTYPE html>
<html lang="en">
<head>
<meta charset="utf-8">
<title>Timeline</title>
<link href="https://fonts.googleapis.com/css2?family=Poppins:wght@400;500;600;700&display=swap" rel="stylesheet">
<style>
  :root {
    --bg: #4a4a4a;
    --card: #3b3b3b;
    --back-btn: #5a5a5a;
    --white: #ffffff;
    --muted: #d6d6d6;
    --blue: #5b9bcb;
    --blue-strong: #5589c4;
    --pink: #c04d77;
    --purple: #5b4a9c;
    --rail: #6a6a6a;
    --node-fill: #f2f2f2;
    --node-ring: #cfcfcf;
    --node-text: #a8a8a8;
  }
  * { margin: 0; padding: 0; box-sizing: border-box; }
  html, body { width: 1200px; height: 756px; overflow: hidden; }
  body {
    background: var(--bg);
    font-family: "Poppins", sans-serif;
    color: var(--white);
    position: relative;
  }
  .brand {
    position: absolute; left: 89px; top: 18px;
    font-size: 27px; font-weight: 700; letter-spacing: -0.3px;
  }
  .theme-toggle {
    position: absolute; left: 896px; top: 29px;
    width: 57px; height: 25px; border-radius: 13px;
    background: var(--white);
  }
  .theme-toggle .knob {
    position: absolute; left: 4px; top: 3px;
    width: 19px; height: 19px; border-radius: 50%;
    background: #3d3d3d;
  }
  .theme-toggle svg { position: absolute; right: 8px; top: 6px; }
  .user {
    position: absolute; left: 980px; top: 20px;
    display: flex; align-items: center; gap: 9px;
  }
  .user .avatar {
    width: 42px; height: 42px; border-radius: 50%;
    background: var(--blue);
    display: flex; align-items: center; justify-content: center;
    font-size: 17px; font-weight: 600;
  }
  .user .greeting { font-size: 13px; font-weight: 600; }
  .user svg { margin-left: 2px; }

  .page-head {
    position: absolute; left: 89px; top: 102px;
    display: flex; align-items: center; gap: 12px;
  }
  .back-btn {
    width: 40px; height: 40px; border-radius: 50%;
    background: var(--back-btn);
    display: flex; align-items: center; justify-content: center;
  }
  .page-title { font-size: 18px; font-weight: 600; }

  .range-filter {
    position: absolute; left: 914px; top: 108px;
    display: flex; gap: 9px;
  }
  .range-filter span {
    width: 59px; height: 33px; border-radius: 3px;
    display: flex; align-items: center; justify-content: center;
    font-size: 13px; font-weight: 600;
  }
  .range-1w { background: var(--blue-strong); }
  .range-1m { background: var(--pink); }
  .range-3m { background: var(--purple); }

  .rail {
    position: absolute; left: 599px; top: 198px;
    width: 2px; height: 435px; background: var(--rail);
  }
  .rail-progress {
    position: absolute; left: 599px; top: 198px;
    width: 3px; height: 160px; background: var(--pink);
  }
  .node {
    position: absolute; left: 585px;
    width: 31px; height: 31px; border-radius: 50%;
    display: flex; align-items: center; justify-content: center;
    font-size: 11px; font-weight: 600;
    background: var(--node-fill); color: var(--node-text);
    border: 2px solid var(--node-ring);
  }
  .node.is-active { background: var(--pink); color: var(--white); border-color: var(--pink); }
  .entry-date {
    position: absolute; right: 642px; top: 232px;
    font-size: 17px; font-weight: 600; color: var(--blue); letter-spacing: 0.3px;
  }
  .entry {
    position: absolute; width: 466px; height: 85px;
    border-radius: 11px; background: var(--card);
    padding: 20px 30px;
  }
  .entry.is-active { background: var(--blue); }
  .entry h3 { font-size: 15px; font-weight: 600; line-height: 22px; }
  .entry p { font-size: 12.5px; color: var(--muted); margin-top: 5px; }
  .entry.is-active p { color: var(--white); }
</style>
</head>
<body>
  <div class="brand">Logo Here</div>

  <div class="theme-toggle">
    <span class="knob"></span>
    <svg width="11" height="12" viewBox="0 0 11 12"><path d="M8 1A5 5 0 1 0 10.5 9 4 4 0 0 1 8 1Z" fill="#bdbdbd"/></svg>
  </div>

  <div class="user">
    <span class="avatar">M</span>
    <span class="greeting">Hi Marlo</span>
    <svg width="10" height="7" viewBox="0 0 10 7"><path d="M1.5 1.5 5 5l3.5-3.5" fill="none" stroke="#ffffff" stroke-width="1.5" stroke-linecap="round"/></svg>
  </div>

  <header class="page-head">
    <span class="back-btn">
      <svg width="7" height="10" viewBox="0 0 7 10"><path d="M5 1.5 2 5l3 3.5" fill="none" stroke="#ffffff" stroke-width="1.5" stroke-linecap="round"/></svg>
    </span>
    <h1 class="page-title">Timeline</h1>
  </header>

  <nav class="range-filter">
    <span class="range-1w">1W</span>
    <span class="range-1m">1M</span>
    <span class="range-3m">3M</span>
  </nav>

  <div class="rail"></div>
  <div class="rail-progress"></div>

  <div class="entry-date">08-10-2022</div>
  <div class="node is-active" style="top:229px">01</div>
  <article class="entry is-active" style="left:644px; top:201px">
    <h3>Cliff Incoming</h3>
    <p>After lunch, there were some problems at home. Found out...</p>
  </article>

  <div class="node" style="top:358px">02</div>
  <article class="entry" style="left:92px; top:331px">
    <h3>Mirror Awakening</h3>
    <p>After lunch, there were some problems at home. Found out...</p>
  </article>

  <div class="node" style="top:489px">03</div>
  <article class="entry" style="left:644px; top:461px">
    <h3>Cliff Incoming</h3>
    <p>After lunch, there were some problems at home. Found out...</p>
  </article>
</body>
</html>
```